Design Direction Exploration for Brand Deliverables

Here is the link to the finalized logo. If you have a design in this project, please use this version of the logo.

https://files.quorvane.net/get/QmRtPzKdYw

Here's the new web address: tidalharpnarrators.com

I need a business card, a Chainlink Business Banner, a set of slides ("Opening Title slide and the "Thank You" slide), and two social media posts created in accordance with the current brand guidelines for "TidalHarp Narrators | For the Rivers Field". These deliverables should be made within Pintora so I can use them.

Target Market(s)

Professionals in the water sector. TidalHarp is a curated platform that connects water-focused organizations—NGOs, environmental firms, public utilities, and innovators—with exceptional voice actors. Our aim is to elevate the use of voice in storytelling across the water sector, from documentaries and e-learning to product launches and advocacy campaigns. This model puts voice actors first while also responding to a sector with growing communication needs.

Industry/Entity Type

TidalHarp Narrators | For the Rivers Field is the go-to authority in voice talent for the global water industry. Unlike traditional agencies, TidalHarp operates as a highly curated platform, connecting water and environment-focused firms, organizations, innovators, and advocates with exceptional human voice actors who bring clarity, credibility, and impact to their communication. From documentaries and promos to e-learning and product launches, our talent delivers performances at industry rates that engage audiences and elevate the stories shaping the future of water. By focusing exclusively on the water sector, TidalHarp ensures every client gains not only access to world-class voice actors but also a partner who understands the urgency and importance of their mission.

Font styles to use
Other font styles liked:
• See brand guidelines.

Colors

Designer to choose colors to be used in the design.

Requirements
Must have
• The elements of the three page brand guidelines: typeface, color palette, secondary element, and recommendation on photo usage.
Nice to have
• Use the three-page brand guidelines to influence your work. The products should feel high-end, inspirational, modern. If it were a home, it would be featured in Dwelling Quarterly. If it were a specific look, it would be featured in Flair. It's the Valtrane of voice talent. Luxurious, trustworthy, the go-to authority. I like some dimensionality/watermarks.
Should not have
• Cheap looking anything. The brand guidelines is a placeholder that I put together. I will update it based on what design this project yields.

```html
<!DOCTYPE html>
<html lang="en">
<head>
<meta charset="utf-8">
<title>TidalHarp Narrators – Social Posts</title>
<link href="https://fonts.googleapis.com/css2?family=Poppins:wght@500;600&display=swap" rel="stylesheet">
<style>
  :root {
    --page-bg: #ffffff;
    --photo-top: #76808a;
    --photo-mid: #3d4a59;
    --photo-deep: #0b1629;
    --brand-white: #ffffff;
    --mint: #a9ddd7;
    --mint-soft: rgba(169, 221, 215, 0.35);
  }
  html, body {
    margin: 0;
    padding: 0;
    width: 1200px;
    height: 675px;
    overflow: hidden;
    background: var(--page-bg);
  }
  .canvas {
    position: relative;
    width: 1200px;
    height: 675px;
    font-family: "Poppins", sans-serif;
  }
  .post {
    position: absolute;
    border-radius: 30px;
    overflow: hidden;
  }
  .post--square { left: 180px; top: 152px; width: 339px; height: 340px; }
  .post--portrait { left: 657px; top: 120px; width: 342px; height: 420px; }

  .post__photo {
    position: absolute;
    inset: 0;
    background:
      linear-gradient(90deg, rgba(11,22,41,0.55) 0%, rgba(11,22,41,0) 45%),
      linear-gradient(180deg, var(--photo-top) 0%, var(--photo-mid) 45%, var(--photo-deep) 88%);
  }
  .brand {
    position: absolute;
    display: flex;
    align-items: center;
    gap: 10px;
    color: var(--brand-white);
    font-weight: 600;
    font-size: 25px;
    line-height: 1.12;
  }
  .brand__dot {
    width: 28px;
    height: 28px;
    border-radius: 50%;
    background: var(--brand-white);
    flex: none;
  }
  .post--square .brand { left: 16px; top: 20px; }
  .post--portrait .brand { left: 22px; top: 16px; }

  .post__headline {
    position: absolute;
    margin: 0;
    color: var(--mint);
    font-weight: 600;
    font-size: 15.5px;
    line-height: 18.2px;
    white-space: nowrap;
  }
  .post--square .post__headline { left: 58px; top: 149px; }
  .post--portrait .post__headline { left: 63px; top: 166px; }

  .post__waves {
    position: absolute;
    right: 0;
    height: 11px;
    background: linear-gradient(90deg, var(--mint-soft), rgba(169, 221, 215, 0.2));
    border-radius: 2px;
  }
  .post--square .post__waves { left: 59px; top: 284px; }
  .post--portrait .post__waves { left: 61px; top: 321px; }
</style>
</head>
<body>
<div class="canvas">

  <article class="post post--square">
    <div class="post__photo" role="img" aria-label="Overhead photo of commuters walking across a tiled concourse, fading into deep navy"></div>
    <div class="brand"><span class="brand__dot"></span><span>TidalHarp<br>Narrators</span></div>
    <p class="post__headline">Slide Title Lorem<br>ipsum dolar sur. Slide<br>Title Lorem.<br>Wipsum dolar sur<br>Slide Title Lorem<br>ipsum dolar sur</p>
    <div class="post__waves" role="img" aria-label="Double wavy line ornament"></div>
  </article>

  <article class="post post--portrait">
    <div class="post__photo" role="img" aria-label="Overhead photo of commuters walking across a tiled concourse, fading into deep navy"></div>
    <div class="brand"><span class="brand__dot"></span><span>TidalHarp<br>Narrators</span></div>
    <p class="post__headline">Slide Title Lorem<br>ipsum dolar sur. Slide<br>Title Lorem.<br>Wipsum dolar sur<br>Slide Title Lorem<br>ipsum dolar sur</p>
    <div class="post__waves" role="img" aria-label="Double wavy line ornament"></div>
  </article>

</div>
</body>
</html>
```